Brookvale Landscape & Construction Website

I have created a detailed txt document and included it in the files upload that will provide all the project details because trying to list it in here is cumbersome. This is for a website only. I have my own team to handle the psd to html conversion. They have an existing website which I have added in the doc. I have also upload various logo files to be used.

Industry/Entity Type

Landscape and Construction

Number of Pages Required

1 page

```html
<!DOCTYPE html>
<html lang="en">
<head>
<meta charset="utf-8">
<title>Brookvale Landscape &amp; Construction</title>
<link href="https://fonts.googleapis.com/css2?family=Playfair+Display:wght@700;800&family=Quicksand:wght@400;500;600&display=swap" rel="stylesheet">
<style>
:root{
  --orange:#f7a600;
  --heading:#f2a20c;
  --red:#d0021b;
  --ink:#222;
  --muted:#444;
  --white:#fff;
  --line:#e6e6e6;
}
*{box-sizing:border-box;margin:0;padding:0}
html,body{width:1200px;height:3771px;overflow:hidden;background:var(--white)}
body{position:relative;font-family:'Quicksand',sans-serif;color:var(--ink)}
.abs{position:absolute}
.brand{display:flex;align-items:center;gap:10px;font-family:'Quicksand',sans-serif;font-weight:600;color:var(--orange);font-size:30px;letter-spacing:.5px}
.brand-dot{width:34px;height:34px;border-radius:50%;background:var(--red)}
.site-header{left:0;top:0;width:1200px;height:105px;border-bottom:1px solid var(--line)}
.site-header .brand{position:absolute;left:0;right:0;top:12px;justify-content:center}
.main-nav{position:absolute;top:72px;left:0;width:1200px;display:flex;justify-content:center;gap:0}
.main-nav a{font-size:14px;color:#333;text-decoration:none;margin:0 21px}
.main-nav a.active{color:var(--orange)}
.hero{left:0;top:105px;width:1200px;height:532px;background:linear-gradient(180deg,#7c8a3a 0%,#5f8a2a 35%,#4d8c22 60%,#3f7a1c 100%)}
.hero-copy{position:absolute;left:0;right:0;top:152px;text-align:center;color:var(--white)}
.hero-copy .kicker{font-family:'Playfair Display',serif;font-weight:700;font-size:26px}
.hero-copy h1{font-family:'Playfair Display',serif;font-weight:700;font-size:58px;line-height:1.1}
.hero-copy p{font-size:16px;line-height:27px;margin-top:10px}
.btn{display:inline-block;background:var(--orange);color:var(--ink);border-radius:20px;font-size:14px;text-align:center;text-decoration:none}
.hero-copy .btn{width:162px;height:38px;line-height:38px;margin-top:14px;color:#333}
.arrow{position:absolute;width:26px;height:26px}
.dots{position:absolute;top:485px;left:0;right:0;display:flex;justify-content:center;gap:5px;align-items:center}
.dots span{width:6px;height:6px;border-radius:3px;background:var(--white)}
.dots span.on{width:18px}
.service-card{top:733px;width:431px;height:296px;border-radius:16px;overflow:hidden;background:linear-gradient(135deg,#d9a23a,#c58a25 60%,#e0b050)}
.service-card .icon{position:absolute;left:50%;top:63px;margin-left:-50px;width:100px;height:100px;border-radius:50%;border:2px dashed rgba(255,255,255,.85);display:flex;align-items:center;justify-content:center}
.service-card .icon span{width:82px;height:82px;border-radius:50%;background:radial-gradient(circle at 40% 35%,#f26a2a,#d0021b)}
.service-card h2{position:absolute;left:0;right:0;top:158px;text-align:center;font-family:'Playfair Display',serif;font-size:36px;color:var(--white)}
.about-photo{left:146px;top:1152px;width:289px;height:260px;border-radius:38px 38px 0 0;background:linear-gradient(135deg,#3f8f2a,#6fb640 60%,#4c9a2c)}
.section-title{font-family:'Playfair Display',serif;font-weight:700;color:var(--heading);font-size:32px}
.about{left:496px;top:1128px;width:560px}
.about p{font-size:16.5px;line-height:27px;color:var(--muted);text-align:justify;margin-top:20px}
.about .btn{width:161px;height:40px;line-height:40px;margin-top:26px;color:#333}
.centered{left:0;width:1200px;text-align:center}
.tile{width:130px;height:124px;border-radius:14px}
.tile-label{width:150px;text-align:center;font-size:16px;color:var(--ink);line-height:24px}
.contact-box{left:0;top:2169px;width:549px;height:417px;background:var(--orange)}
.map{left:511px;top:2137px;width:689px;height:482px;background:linear-gradient(135deg,#d8d8d8,#cfd7c4 45%,#d4d4d4 70%,#a9cbe0);box-shadow:0 4px 12px rgba(0,0,0,.2)}
.contact-text{left:146px;top:2253px;width:360px;font-size:16px;line-height:24px;color:#222}
.contact-list{list-style:none;margin-top:50px}
.contact-list li{display:flex;gap:8px;align-items:flex-start;line-height:27px}
.contact-list svg{flex:none;margin-top:8px}
.photo{border-radius:0}
.see-more{left:844px;top:3214px;width:176px;height:39px;border:2px solid var(--white);border-radius:20px;color:var(--white);font-size:16px;font-weight:600;text-align:center;line-height:35px}
.footer-brand{left:0;width:1200px;top:3522px;justify-content:center}
.footer-copy{top:3590px;font-size:16px;line-height:28px;color:#333}
.footer-nav{left:0;top:3661px;width:1200px;height:46px;background:var(--orange);display:flex;justify-content:center;align-items:center}
.footer-nav a{font-size:14px;color:#333;text-decoration:none;margin:0 21px}
.follow{left:142px;top:3731px;font-size:12px;color:#333;display:flex;gap:8px;align-items:center}
.follow i{width:11px;height:11px;border-radius:50%;background:#222;display:inline-block}
.copyright{right:144px;top:3731px;font-size:12px;color:#333}
</style>
</head>
<body>

<header class="abs site-header">
  <div class="brand"><span class="brand-dot"></span>Brookvale</div>
  <nav class="main-nav">
    <a class="active" href="#">Home</a><a href="#">Landscape Services</a><a href="#">Construction Services</a><a href="#">Company</a><a href="#">Contact</a><a href="#">FAQs</a><a href="#">Gallery</a>
  </nav>
</header>

<section class="abs hero" role="img" aria-label="Close-up of a freshly mown green lawn">
  <svg class="arrow" style="left:66px;top:240px" viewBox="0 0 26 26"><path d="M17 3 7 13l10 10" fill="none" stroke="#fff" stroke-width="3"/></svg>
  <svg class="arrow" style="left:1092px;top:240px" viewBox="0 0 26 26"><path d="M9 3l10 10L9 23" fill="none" stroke="#fff" stroke-width="3"/></svg>
  <div class="hero-copy">
    <div class="kicker">Welcome to</div>
    <h1>Brookvale</h1>
    <p>Lorem ipsum dolor sit amet, consectetur adipiscing elit, sed<br>do eiusmod tempor et dolore magna aliqua.</p>
    <a class="btn" href="#">Get Started</a>
  </div>
  <div class="dots"><span></span><span class="on"></span><span></span><span></span></div>
</section>

<a class="abs service-card" style="left:146px" role="img" aria-label="Sod being laid beside a gravel path">
  <div class="icon"><span></span></div>
  <h2>Landscape Services</h2>
</a>
<a class="abs service-card" style="left:622px" role="img" aria-label="Builders reviewing plans with a hard hat">
  <div class="icon" style="top:63px"><span></span></div>
  <h2 style="top:168px">Construction Services</h2>
</a>

<div class="abs about-photo" role="img" aria-label="Lawn mower on green grass"></div>
<section class="abs about">
  <h2 class="section-title">About Us</h2>
  <p>Brookvale Landscape &amp; Construction Inc. is a year round, full service residential and commercial licensed construction company and landscape/hardscape installer. Our construction consists of custom decks, screen rooms, three- and four-season additions, remodels, foundation repair, roofing and siding, soffits, gutters, windows and doors. We also build pole barns, garages and cabins.</p>
  <a class="btn" href="#">Read More</a>
</section>

<h2 class="abs centered section-title" style="top:1494px">Landscaping Services</h2>
<svg class="arrow" style="left:66px;top:1610px" viewBox="0 0 26 26"><path d="M17 3 7 13l10 10" fill="none" stroke="#d0021b" stroke-width="3"/></svg>
<svg class="arrow" style="left:1092px;top:1610px" viewBox="0 0 26 26"><path d="M9 3l10 10L9 23" fill="none" stroke="#d0021b" stroke-width="3"/></svg>
<div class="abs tile" style="left:146px;top:1573px;background:linear-gradient(135deg,#9a9a9a,#c9c4bb)" role="img" aria-label="Paver stones being laid"></div>
<div class="abs tile" style="left:301px;top:1573px;background:linear-gradient(135deg,#6d6a66,#9c9893)" role="img" aria-label="Stacked boulder wall"></div>
<div class="abs tile" style="left:457px;top:1573px;background:linear-gradient(135deg,#3d7a2c,#3a9db4 60%,#6aa64a)" role="img" aria-label="Garden pond with plants"></div>
<div class="abs tile" style="left:612px;top:1573px;background:linear-gradient(135deg,#4f7a35,#9d8f74 60%,#5b8a3c)" role="img" aria-label="Stone waterfall in a garden"></div>
<div class="abs tile" style="left:768px;top:1573px;background:linear-gradient(135deg,#5e9a38,#8b7656 60%,#6aa844)" role="img" aria-label="Roll of sod being laid"></div>
<div class="abs tile" style="left:923px;top:1573px;background:linear-gradient(135deg,#6a8f4a,#8a7a58 55%,#c9a52a)" role="img" aria-label="Excavator grading a yard"></div>
<div class="abs tile-label" style="left:136px;top:1722px">Paver</div>
<div class="abs tile-label" style="left:288px;top:1709px">Boulder<br>Walls</div>
<div class="abs tile-label" style="left:444px;top:1722px">Ponds</div>
<div class="abs tile-label" style="left:603px;top:1722px">Waterfalls</div>
<div class="abs tile-label" style="left:753px;top:1722px">Sod</div>
<div class="abs tile-label" style="left:920px;top:1709px">Grading /<br>Excavating</div>

<h2 class="abs centered section-title" style="top:1796px">Construction Services</h2>
<svg class="arrow" style="left:66px;top:1936px" viewBox="0 0 26 26"><path d="M17 3 7 13l10 10" fill="none" stroke="#d0021b" stroke-width="3"/></svg>
<svg class="arrow" style="left:1092px;top:1936px" viewBox="0 0 26 26"><path d="M9 3l10 10L9 23" fill="none" stroke="#d0021b" stroke-width="3"/></svg>
<div class="abs tile" style="left:146px;top:1875px;background:linear-gradient(135deg,#3f7fc0,#a0522d 55%,#c47a4a)" role="img" aria-label="Wooden deck with pergola"></div>
<div class="abs tile" style="left:301px;top:1875px;background:linear-gradient(135deg,#3a3a3a,#8a8a8a 55%,#4a4a4a)" role="img" aria-label="Heated footing tubing layout"></div>
<div class="abs tile" style="left:457px;top:1875px;background:linear-gradient(135deg,#c59060,#9a6a3e 55%,#d9b48a)" role="img" aria-label="Timber framed house addition"></div>
<div class="abs tile" style="left:612px;top:1875px;background:linear-gradient(135deg,#8aa8c8,#e8e8e8 50%,#6f8a5a)" role="img" aria-label="Pole barn with porch"></div>
<div class="abs tile" style="left:768px;top:1875px;background:linear-gradient(135deg,#6e6256,#3a2a1e 50%,#e07a2a)" role="img" aria-label="Cabin interior with stone fireplace"></div>
<div class="abs tile" style="left:923px;top:1875px;background:linear-gradient(135deg,#d8d2c8,#9a8e80 60%,#c8c0b4)" role="img" aria-label="Room under remodel"></div>
<div class="abs tile-label" style="left:132px;top:2016px">Decks</div>
<div class="abs tile-label" style="left:288px;top:2014px">Footings</div>
<div class="abs tile-label" style="left:444px;top:2016px">Additions</div>
<div class="abs tile-label" style="left:606px;top:2016px">Pole Barns</div>
<div class="abs tile-label" style="left:760px;top:2016px">Cabins</div>
<div class="abs tile-label" style="left:913px;top:2016px">Remodels</div>

<div class="abs contact-box"></div>
<div class="abs map" role="img" aria-label="Street map of the service area in Minnesota"></div>
<section class="abs contact-text">
  <p>If you wish to contact us by e-mail, fax, phone or letter, please contact us at:</p>
  <ul class="contact-list">
    <li><svg width="11" height="13" viewBox="0 0 11 13"><path d="M5.5 0A5 5 0 0 0 .5 5c0 3.5 5 8 5 8s5-4.5 5-8a5 5 0 0 0-5-5zm0 7a2 2 0 1 1 0-4 2 2 0 0 1 0 4z" fill="#d0021b"/></svg><span>Brookvale Landscape &amp; Construction Inc<br>1420 – 118th Ave NE<br>Cedar Hollow, MN&nbsp; 55099</span></li>
    <li><svg width="11" height="11" viewBox="0 0 11 11"><path d="M2.2 0 4 2.6 2.9 4a6 6 0 0 0 4.1 4.1L8.4 7 11 8.8 9.7 11C4.6 10.6.4 6.4 0 1.3z" fill="#d0021b"/></svg><span>555.014.2297</span></li>
    <li><svg width="11" height="9" viewBox="0 0 11 9"><rect width="11" height="9" fill="#d0021b"/><path d="M0 0l5.5 5L11 0" fill="none" stroke="#f7a600" stroke-width="1.2"/></svg><span>dana@brookvalelandscape.com</span></li>
  </ul>
</section>

<h2 class="abs centered section-title" style="top:2717px">Gallery</h2>
<div class="abs photo" style="left:120px;top:2802px;width:300px;height:205px;background:linear-gradient(135deg,#3e5a2a,#b08050 55%,#8a6040)" role="img" aria-label="Composite deck with railing"></div>
<div class="abs photo" style="left:120px;top:3035px;width:301px;height:408px;background:linear-gradient(135deg,#7a8a90,#5a3a22 55%,#9a8a80)" role="img" aria-label="Wooden staircase with iron balusters"></div>
<div class="abs photo" style="left:454px;top:2802px;width:298px;height:409px;background:linear-gradient(160deg,#4a5868,#5f8a3a 45%,#a8a49a 75%)" role="img" aria-label="Stamped stone walkway beside a house"></div>
<div class="abs photo" style="left:454px;top:3239px;width:298px;height:204px;background:linear-gradient(160deg,#b8b4aa,#8a7e72 50%,#5e8a3a)" role="img" aria-label="Boulder landscaping bed"></div>
<div class="abs photo" style="left:786px;top:2802px;width:298px;height:205px;background:linear-gradient(160deg,#7a9a5a,#e8e2cc 45%,#5a6a3a 70%,#8a7a5a)" role="img" aria-label="Cream pole barn with green trim"></div>
<div class="abs photo" style="left:786px;top:3035px;width:298px;height:408px;background:linear-gradient(160deg,#e6b430,#d9a21a 55%,#e8b840)" role="img" aria-label="Stone walkway beneath an orange overlay"></div>
<div class="abs see-more">See More</div>

<div class="abs brand footer-brand"><span class="brand-dot"></span>Brookvale</div>
<p class="abs centered footer-copy">Brookvale Landscape &amp; Construction Inc. is a year round, full service residential and commercial licensed construction<br>company and landscape/hardscape installer.</p>
<nav class="abs footer-nav">
  <a href="#">Home</a><a href="#">Landscape Services</a><a href="#">Construction Services</a><a href="#">Company</a><a href="#">Contact</a><a href="#">FAQs</a><a href="#">Gallery</a>
</nav>
<div class="abs follow">Follow us :<i></i><i></i><i></i></div>
<div class="abs copyright">© copyrights 2022&nbsp; Brookvale Landscape &amp; Constructions|&nbsp; All Rights Reserved</div>

</body>
</html>
```